Pellinex header in combination with existing logo

The header of the Pellinex profile% 26quot; https: //www.pellinex.com/company/morvadaconsulting%26quot; shall be renewed. Therefore, a new background image shall be designed. A design is simple, clear, well structured and fits the consulting business. This article should be used as a separate project for publications. It will become the corporate identity for social media and employer branding. In case you have any questions, feel free to contact us.b ***************** * Background *: MORVADA is a leading international management consultancy for operations. With unique concepts and the right employees, we achieve effective results. We support well-known companies from industry and trade in the optimization of the total value-added chain all over the world. Our custom-tailored approach enables us to quickly optimize our customer's processes along the value-added chain. Morvada works in the following branches: - Automotive / Automotive supplier - Pharmaceutical - Foundry - Shipyard - Steel industry - Consumer goods - Energy - Engineering - Electronics - Facility engineering% 26amp; construction

Target Market(s)

Consulting / Industry (Pharmaceutical, productive industry, metal, shipbuilding, automotive)

Industry/Entity Type

Management Consulting

Font styles to use
Other font styles liked:
• see PPT

Colors

Designer to choose colors to be used in the design.

Requirements
Must have
• Please follow the recommended Pellinex resolution guideline (see also: Pellinex_Guideline.jpg). Rectangular background (see page 26) kelm_award_list% 26quot; kelm_award_list% 26quot;, three sizes next to each other) right.
Nice to have
• PowerPoint presentation as a guideline however, not as a must have in case you want to use images. You want to find various available licensed pictures. These can be used, but we believe that a simple and neutral (abstract?) Background image would be better. - 26gt%; You are also considered if you do not use one of the provided pictures at all! We want to test a simplistic design as well. Convince us!

```html
<!DOCTYPE html>
<html lang="en">
<head>
<meta charset="utf-8">
<title>Morvada Management Consulting – Pellinex Header</title>
<link rel="stylesheet" href="https://fonts.googleapis.com/css2?family=Open+Sans:wght@400;600;700&display=swap">
<style>
  :root {
    --charcoal: #474646;
    --charcoal-dark: #3e3d3d;
    --facet-light: #555454;
    --facet-mid: #4c4b4b;
    --brand-red: #d20f2d;
    --brand-red-deep: #a3091f;
    --brand-red-dark: #8a0b1c;
    --frame-line: #9a9999;
    --label-grey: #8f8e8e;
    --white: #ffffff;
  }
  html, body {
    margin: 0;
    padding: 0;
    width: 1200px;
    height: 364px;
    overflow: hidden;
    background: var(--charcoal);
  }
  .header-canvas {
    position: relative;
    width: 1200px;
    height: 364px;
    overflow: hidden;
    font-family: "Open Sans", Arial, sans-serif;
  }
  .header-art {
    position: absolute;
    inset: 0;
    display: block;
  }
  .cut-frame-label {
    position: absolute;
    left: 205px;
    top: 18px;
    margin: 0;
    font-size: 20px;
    font-weight: 600;
    letter-spacing: 0.2px;
    color: var(--label-grey);
    line-height: 1;
  }
  .brand-lockup {
    position: absolute;
    left: 250px;
    top: 76px;
    color: var(--white);
  }
  .brand-name {
    margin: 0;
    font-size: 32px;
    font-weight: 700;
    letter-spacing: 1px;
    line-height: 1;
  }
  .brand-tagline {
    margin: 4px 0 0 60px;
    font-size: 13px;
    font-weight: 400;
    line-height: 1;
    white-space: nowrap;
  }
</style>
</head>
<body>
  <main class="header-canvas">
    <svg class="header-art" width="1200" height="364" viewBox="0 0 1200 364" xmlns="http://www.w3.org/2000/svg">
      <defs>
        <linearGradient id="photo-tone" x1="0" y1="0" x2="1" y2="0.3">
          <stop offset="0" stop-color="#fbe6d6"/>
          <stop offset="0.45" stop-color="#f6c2a8"/>
          <stop offset="0.7" stop-color="#ee7f63"/>
          <stop offset="0.88" stop-color="#e9a7ae"/>
          <stop offset="1" stop-color="#c9a9ad"/>
        </linearGradient>
        <linearGradient id="photo-veil" x1="0" y1="0" x2="1" y2="0">
          <stop offset="0" stop-color="#ffffff" stop-opacity="0.55"/>
          <stop offset="0.5" stop-color="#ffffff" stop-opacity="0.1"/>
          <stop offset="1" stop-color="#ffffff" stop-opacity="0"/>
        </linearGradient>
      </defs>

      <g class="charcoal-facets">
        <rect width="1200" height="364" fill="var(--charcoal)"/>
        <polygon points="0,0 520,0 0,36" fill="var(--charcoal-dark)"/>
        <polygon points="0,110 260,160 420,364 0,364" fill="var(--facet-light)" opacity="0.6"/>
        <polygon points="0,190 150,364 0,364" fill="var(--facet-mid)"/>
        <polygon points="260,160 500,60 420,364" fill="var(--facet-mid)" opacity="0.7"/>
        <polygon points="290,225 520,210 430,364" fill="var(--facet-light)" opacity="0.5"/>
      </g>

      <g class="red-band">
        <polygon points="519,0 660,0 545,364 408,364" fill="var(--brand-red)"/>
        <polygon points="519,0 660,0 620,120 500,60" fill="var(--brand-red-dark)" opacity="0.6"/>
        <polygon points="440,280 545,364 408,364" fill="var(--brand-red-deep)"/>
      </g>

      <g class="photo-area" role="img" aria-label="Photo area: hands holding a tablet above an open laptop on a desk, in warm red and cream tones">
        <polygon points="648,0 1200,0 1200,364 543,364" fill="url(#photo-tone)"/>
        <polygon points="648,0 990,0 870,364 543,364" fill="url(#photo-veil)"/>
        <polygon points="560,310 1200,240 1200,364 545,364" fill="var(--brand-red-deep)" opacity="0.35"/>
      </g>

      <rect class="cut-frame" x="207.5" y="45.5" width="786" height="276" fill="none" stroke="var(--frame-line)" stroke-width="1.5"/>
    </svg>

    <p class="cut-frame-label">PELLINEX CUT FRAME</p>

    <div class="brand-lockup">
      <p class="brand-name">MORVADA</p>
      <p class="brand-tagline">Management Consulting</p>
    </div>
  </main>
</body>
</html>
```